BUSINESS CARDS, ENVELOPE, LETTER HEADS AND OTHER STATIONARY
FOR BROOKFERN DATA TECHNOLOGY
I need double sided standard sized Business Card [3.5" x 2"]
Please show me a wide variey of fonts including the ones from the logo
Bright & Fun-filled
Dorian Velmont
Solutions Architect / Technical Sales
82 Pinewhistle Crescent SW
Calgary, Alberta
Canada T2K7M5
dorianv@brookferndataworks.example
http://www.brookferndataworks.example
On the Back of the Bussiness Card I would like to describe a few of the features and solutions that Brookfern Data provides like:
- Electronic Records Management
-IT Solutions (Hardware / Software)
- After hours Technical support (Disaster Recover)
- Procurement
Logo
LOGO file 2
Please Do Not Include the Reflection as part of the logo Thank You

```html
<!DOCTYPE html>
<html lang="en">
<head>
<meta charset="utf-8">
<title>Brookfern Data Technology – Stationery Set</title>
<link href="https://fonts.googleapis.com/css2?family=Open+Sans:wght@400;600;700&display=swap" rel="stylesheet">
<style>
  :root{
    --bg:#e9eaeb;
    --paper:#ffffff;
    --navy:#16345f;
    --blue:#1f5fa8;
    --blue-light:#3b8fd4;
    --green:#8cc63f;
    --grey-text:#6b6f74;
    --line:#9aa0a6;
    --globe-a:#dfe4e7;
    --globe-b:#f3f5f6;
  }
  *{box-sizing:border-box;margin:0;padding:0}
  html,body{width:1200px;height:552px;overflow:hidden}
  body{background:var(--bg);font-family:"Open Sans",Arial,sans-serif;color:var(--grey-text);position:relative}
  .piece{position:absolute;background:var(--paper);overflow:hidden;box-shadow:0 1px 3px rgba(0,0,0,.18)}
  .edge-art{position:absolute;inset:0;width:100%;height:100%}
  .globe{position:absolute;border-radius:50%;background:radial-gradient(circle at 40% 38%,var(--globe-b),var(--globe-a) 70%,#d2d9dd)}
  .brand{position:absolute;display:flex;align-items:center;gap:5px;font-weight:700;color:var(--navy);white-space:nowrap}
  .brand .dot{border-radius:50%;background:var(--blue)}
  .small{position:absolute;font-size:5px;line-height:7px;color:var(--grey-text)}

  /* fax sheet */
  .fax{left:34px;top:24px;width:355px;height:509px}
  .fax .brand{left:12px;top:14px;font-size:12px}
  .fax .brand .dot{width:14px;height:14px}
  .fax-label{position:absolute;right:22px;top:34px;font-size:7px;font-weight:700;color:#333}
  .fax-table{position:absolute;left:12px;top:44px;width:316px;border:1px solid #555;border-collapse:collapse;font-size:6px;color:#333}
  .fax-table td{border:1px solid #555;height:16px;padding:0 4px}
  .fax-table td.lbl{width:34px}
  .fax-checks{position:absolute;left:12px;top:129px;display:flex;gap:14px;font-size:5.5px;color:#333}
  .fax-checks span::before{content:"";display:inline-block;width:6px;height:6px;border:1px solid #555;margin-right:4px;vertical-align:-1px}
  .fax .small{left:12px;bottom:14px}

  /* letterhead */
  .letterhead{left:403px;top:24px;width:360px;height:509px}
  .letterhead .brand{left:12px;top:14px;font-size:12px}
  .letterhead .brand .dot{width:14px;height:14px}
  .letterhead .small{left:12px;bottom:14px}

  /* business cards */
  .card-front{left:775px;top:29px;width:161px;height:91px;background:linear-gradient(160deg,var(--blue-light),var(--blue) 45%,var(--navy))}
  .card-front .person{position:absolute;left:8px;top:8px;color:#fff;font-size:5px;line-height:7px}
  .card-front .person b{font-size:6px;display:block}
  .card-front .brand{left:8px;top:50px;font-size:7px;color:#fff}
  .card-front .brand .dot{width:8px;height:8px;background:#fff}
  .card-back{left:943px;top:29px;width:161px;height:91px}
  .card-back .brand{left:52px;top:8px;font-size:7px}
  .card-back .brand .dot{width:8px;height:8px}
  .card-back .services{position:absolute;left:52px;top:24px;font-size:4.2px;line-height:6.5px;list-style:none;color:var(--grey-text)}
  .card-back .services li::before{content:"■ ";color:var(--green)}

  /* envelopes */
  .env-front{left:778px;top:137px;width:391px;height:199px}
  .env-front .brand{left:12px;top:12px;font-size:10px}
  .env-front .brand .dot{width:12px;height:12px}
  .env-front .small{left:12px;top:34px}
  .env-back{left:778px;top:355px;width:391px;height:173px}
  .env-back .flap{position:absolute;inset:0;width:100%;height:100%}
  .env-back .brand{left:50%;top:50px;transform:translateX(-50%);font-size:11px}
  .env-back .brand .dot{width:12px;height:12px}
</style>
</head>
<body>

<!-- Fax sheet -->
<section class="piece fax">
  <div class="globe" role="img" aria-label="Faint globe with circling arrow illustration" style="left:175px;top:225px;width:190px;height:190px"></div>
  <svg class="edge-art" viewBox="0 0 355 509" preserveAspectRatio="none" aria-hidden="true">
    <defs><linearGradient id="bandA" x1="0" y1="0" x2="0" y2="1"><stop offset="0" stop-color="#3b8fd4"/><stop offset="1" stop-color="#16345f"/></linearGradient></defs>
    <path d="M340 0H355V509H170C260 492 330 430 338 320Z" fill="url(#bandA)"/>
    <path d="M336 0V320C328 430 258 492 160 509" fill="none" stroke="#8cc63f" stroke-width="2"/>
  </svg>
  <div class="brand"><span class="dot"></span>Brookfern Data</div>
  <div class="fax-label">FAX</div>
  <table class="fax-table">
    <tr><td class="lbl">To:</td><td></td><td class="lbl">From:</td><td></td></tr>
    <tr><td class="lbl">Fax:</td><td></td><td class="lbl">Pages:</td><td></td></tr>
    <tr><td class="lbl">Phone:</td><td></td><td class="lbl">Date:</td><td></td></tr>
    <tr><td class="lbl">Re:</td><td></td><td class="lbl">CC:</td><td></td></tr>
  </table>
  <div class="fax-checks"><span>Urgent</span><span>For Review</span><span>Please Comment</span><span>Please Reply</span><span>Please Recycle</span></div>
  <p class="small">82 Pinewhistle Crescent SW<br>Calgary, Alberta<br>Canada T2K7M5<br>dorianv@brookferndataworks.example</p>
</section>

<!-- Letterhead -->
<section class="piece letterhead">
  <div class="globe" role="img" aria-label="Faint globe with circling arrow illustration" style="left:120px;top:150px;width:230px;height:230px"></div>
  <svg class="edge-art" viewBox="0 0 360 509" preserveAspectRatio="none" aria-hidden="true">
    <defs><linearGradient id="bandB" x1="0" y1="0" x2="0" y2="1"><stop offset="0" stop-color="#3b8fd4"/><stop offset="1" stop-color="#16345f"/></linearGradient></defs>
    <path d="M345 0H360V509H170C262 492 335 430 343 320Z" fill="url(#bandB)"/>
    <path d="M341 0V320C333 430 260 492 160 509" fill="none" stroke="#8cc63f" stroke-width="2"/>
  </svg>
  <div class="brand"><span class="dot"></span>Brookfern Data</div>
  <p class="small">82 Pinewhistle Crescent SW<br>Calgary, Alberta<br>Canada T2K7M5<br>http://www.brookferndataworks.example</p>
</section>

<!-- Business card front -->
<section class="piece card-front">
  <svg class="edge-art" viewBox="0 0 161 91" preserveAspectRatio="none" aria-hidden="true">
    <path d="M0 70C50 60 110 75 161 40V91H0Z" fill="#ffffff" opacity=".12"/>
    <path d="M0 72C50 62 110 77 161 42" fill="none" stroke="#8cc63f" stroke-width="1.6"/>
  </svg>
  <div class="globe" role="img" aria-label="Faint globe illustration" style="left:108px;top:8px;width:46px;height:46px;opacity:.35"></div>
  <div class="person"><b>Dorian Velmont</b>Solutions Architect / Technical Sales</div>
  <div class="brand"><span class="dot"></span>Brookfern Data</div>
</section>

<!-- Business card back -->
<section class="piece card-back">
  <svg class="edge-art" viewBox="0 0 161 91" preserveAspectRatio="none" aria-hidden="true">
    <path d="M0 80C60 72 110 86 161 70V91H0Z" fill="#1f5fa8"/>
    <path d="M0 78C60 70 110 84 161 68" fill="none" stroke="#8cc63f" stroke-width="1.4"/>
  </svg>
  <div class="brand"><span class="dot"></span>Brookfern Data</div>
  <ul class="services">
    <li>Electronic Records Management</li>
    <li>IT Solutions (Hardware / Software)</li>
    <li>After hours Technical support</li>
    <li>Procurement</li>
  </ul>
</section>

<!-- Envelope front -->
<section class="piece env-front">
  <div class="globe" role="img" aria-label="Faint globe with circling arrow illustration" style="left:255px;top:55px;width:120px;height:120px"></div>
  <svg class="edge-art" viewBox="0 0 391 199" preserveAspectRatio="none" aria-hidden="true">
    <defs><linearGradient id="bandC" x1="0" y1="0" x2="0" y2="1"><stop offset="0" stop-color="#3b8fd4"/><stop offset="1" stop-color="#16345f"/></linearGradient></defs>
    <path d="M376 0H391V199H250C320 190 370 160 374 110Z" fill="url(#bandC)"/>
    <path d="M372 0V110C368 160 318 190 240 199" fill="none" stroke="#8cc63f" stroke-width="2"/>
  </svg>
  <div class="brand"><span class="dot"></span>Brookfern Data</div>
  <p class="small">82 Pinewhistle Crescent SW<br>Calgary, Alberta<br>Canada T2K7M5</p>
</section>

<!-- Envelope back -->
<section class="piece env-back">
  <svg class="flap" viewBox="0 0 391 173" preserveAspectRatio="none" aria-hidden="true">
    <path d="M0 0H391L220 40Q195 46 170 40Z" fill="#e3e8ee"/>
    <path d="M0 0L170 40Q195 46 220 40L391 0" fill="none" stroke="#c9d0d8" stroke-width="1"/>
  </svg>
  <div class="brand"><span class="dot"></span>Brookfern Data</div>
</section>

</body>
</html>
```